Insight Plus. needs Business Cards

For this project, we need business cards (currently have also put a call out for a logo). We are a start-up called Insight Plus. This is our second company (our first one was called Querivance). Traditionally we have been providing market research services across different sectors, primarily financial services and the pharmaceutical industry. However, we now want to go beyond market research to offer more (Plus.)... strategic consulting and big data knowledge management. We want our brand to be approachable, creative, fun but professional.

Target Market(s)

The target audience is a business professional - we are B2B (business to business) and do not sell our services to individuals. The brands we work with are major brands across industries, but primarily automotive, financial and pharmaceutical.

Industry/Entity Type

Market Research

Font styles to use
Serif
Sans Serif
Other font styles liked:
• Calibri

Requirements
Must have
• Be clean, simple, modern
Show our address and phone number and email address and website URL
We do not need to have titles showing.

```html
<!DOCTYPE html>
<html lang="en">
<head>
<meta charset="utf-8">
<title>Insight Plus. — Business Cards</title>
<link rel="stylesheet" href="https://fonts.googleapis.com/css2?family=Arimo:wght@400;700&display=swap">
<style>
  :root {
    --canvas-bg: #ecebe8;
    --card-dark-1: #555354;
    --card-dark-2: #767473;
    --card-white: #f4f4f4;
    --lime: #c9d94a;
    --text-light: #f1f1f1;
    --text-muted: #d9d9d9;
    --logo-grey: #4d4b4c;
    --rule: rgba(255,255,255,0.75);
  }
  html, body {
    margin: 0;
    width: 1200px;
    height: 886px;
    overflow: hidden;
    background: var(--canvas-bg);
    font-family: "Arimo", Arial, sans-serif;
  }
  .canvas {
    position: relative;
    width: 1200px;
    height: 886px;
  }
  .card {
    position: absolute;
    left: 340px;
    width: 520px;
    height: 297px;
    border-radius: 16px;
    overflow: hidden;
    box-shadow: 0 10px 28px rgba(0,0,0,0.22);
  }
  /* Back of card */
  .card-back {
    top: 110px;
    background: linear-gradient(135deg, var(--card-dark-1), var(--card-dark-2) 55%, var(--card-dark-1));
  }
  .logo-box {
    position: absolute;
    border: 2px solid var(--lime);
    display: flex;
    align-items: center;
    justify-content: center;
    box-sizing: border-box;
  }
  .card-back .logo-box {
    left: 128px;
    top: 88px;
    width: 264px;
    height: 76px;
  }
  .logo-name {
    font-size: 40px;
    font-weight: 400;
    letter-spacing: -0.5px;
    white-space: nowrap;
  }
  .card-back .logo-name { color: var(--lime); }
  .website {
    position: absolute;
    right: 40px;
    bottom: 60px;
    font-size: 13px;
    color: var(--text-light);
    letter-spacing: 0.2px;
  }
  .rule {
    position: absolute;
    left: 0;
    right: 0;
    height: 1px;
    background: var(--rule);
  }
  .rule-1 { bottom: 44px; }
  .rule-2 { bottom: 36px; }

  /* Front of card */
  .card-front {
    top: 480px;
    background: var(--card-white);
  }
  .card-front .logo-box {
    left: 128px;
    top: 40px;
    width: 264px;
    height: 76px;
  }
  .card-front .logo-name { color: var(--logo-grey); }
  .accent-band {
    position: absolute;
    left: 0; right: 0;
    top: 148px;
    height: 10px;
    background: var(--lime);
  }
  .contact-panel {
    position: absolute;
    left: 0; right: 0;
    top: 158px;
    bottom: 0;
    background: linear-gradient(90deg, var(--card-dark-1), var(--card-dark-2));
    padding: 16px 0 0 128px;
    box-sizing: border-box;
  }
  .person-name {
    margin: 0;
    font-size: 17px;
    color: var(--text-light);
  }
  .person-role {
    margin: 2px 0 10px;
    font-size: 12px;
    color: var(--lime);
  }
  .contact-list {
    list-style: none;
    margin: 0;
    padding: 0;
    font-size: 12px;
    line-height: 19px;
    color: var(--text-muted);
  }
</style>
</head>
<body>
  <main class="canvas">
    <section class="card card-back" aria-label="Business card back">
      <div class="logo-box"><span class="logo-name">Insight Plus.</span></div>
      <span class="website">www.insightplus-mr.com</span>
      <div class="rule rule-1"></div>
      <div class="rule rule-2"></div>
    </section>

    <section class="card card-front" aria-label="Business card front">
      <div class="logo-box"><span class="logo-name">Insight Plus.</span></div>
      <div class="accent-band"></div>
      <div class="contact-panel">
        <p class="person-name">Employee Name</p>
        <p class="person-role">Managing Director</p>
        <ul class="contact-list">
          <li>0012 4870 215</li>
          <li>hello@insightplus-mr.com</li>
          <li>14 Harbour Row, Suite 2, Brookfield, USA</li>
        </ul>
      </div>
    </section>
  </main>
</body>
</html>
```